Holiday Rental Company Flyer Design (DL not A5)

Note from PixelFolk Administration: The category sizing selected is A5, however the project requires DL sized artwork. Please refer to the DL template link below while the 'Special Requirements' are updated accordingly.

Project Brief:
We need a double sided DL flyer designed for an up market Holiday Rental Company that portrays a personalised approach to property management. These are to be used for letter box drops to homes we're specifically targeting so the design should be modern, complimentary colour palette, uncluttered & visually appealing.

Please Download the DL Template from Quillmark here: http://www.quillmark.com.au/qm/ns/propath/UploadResources.aspx?selectedTab=0?pfid=BFB&pf_id=BFB&xnav=easypath-upload-image#Templates

Target Market(s)

Wealthy Home Owners

Industry/Entity Type

It Company

Font styles to use
Other font styles liked:
• Avant Garde Extra Light & Demi

Colors
33b8a4

Requirements
Must have
• DL Flyer sizes (210mm width x 99mm width, plus 3mm bleed)
• Front: Logo, Main Image & Grab
• Back: Contact Details & Brief Description of our business
• Images: Ideally the main image should be the house with the pool but alternatively a lifestyle images could also be used.
Nice to have
• A creative designer!
Should not have
• Clutter & busy designs

```html
<!DOCTYPE html>
<html lang="en">
<head>
<meta charset="utf-8">
<title>Harbourline Retreats – DL Flyer Front</title>
<link rel="stylesheet" href="https://fonts.googleapis.com/css2?family=Poppins:wght@200;300;400;600&display=swap">
<style>
  :root {
    --page-bg: #e9eae6;
    --dusk-navy: #2a1f6b;
    --dusk-violet: #5a46a8;
    --wall-lilac: #a28ee0;
    --pool-blue: #3a86e6;
    --warm-amber: #d9a546;
    --warm-mid: #8a6430;
    --warm-deep: #2e2218;
    --panel-mist: #e4eeeb;
    --panel-circle: #f1f7f5;
    --brand-teal: #1ea88a;
    --ink: #262626;
    --ink-soft: #333333;
    --white: #ffffff;
    --pattern-teal: #33b8a4;
    --pattern-light: #8fd6c8;
    --pattern-dark: #1c2a2a;
  }
  * { margin: 0; padding: 0; box-sizing: border-box; }
  html, body {
    width: 1200px; height: 900px; overflow: hidden;
    background: var(--page-bg);
    font-family: "Poppins", sans-serif;
  }
  .flyer {
    position: absolute; left: 72px; top: 200px;
    width: 1058px; height: 495px; overflow: hidden;
    box-shadow: 0 4px 14px rgba(0,0,0,0.18);
  }
  .photo-pool {
    position: absolute; left: 0; top: 0; width: 600px; height: 495px;
    background:
      linear-gradient(180deg, transparent 0%, transparent 78%, var(--pool-blue) 100%),
      linear-gradient(160deg, var(--dusk-navy) 0%, var(--dusk-violet) 60%, #4a3c9a 100%);
  }
  .wall-light {
    position: absolute; left: 0; top: 0; width: 600px; height: 495px;
  }
  .photo-terrace {
    position: absolute; left: 883px; top: 0; width: 175px; height: 495px;
    background: linear-gradient(180deg, #c79645 0%, var(--warm-amber) 35%, var(--warm-mid) 65%, var(--warm-deep) 100%);
  }
  .brand {
    position: absolute; left: 80px; top: 145px; width: 440px;
    color: var(--white); font-weight: 200; font-size: 54px;
    line-height: 1.2; letter-spacing: 0.16em; text-align: center;
  }
  .brand-mark {
    display: block; margin: 30px auto 0;
    width: 60px; height: 60px; border: 2px solid var(--white); border-radius: 50%;
  }
  .grab-panel {
    position: absolute; left: 600px; top: 0; width: 283px; height: 348px;
    background: var(--panel-mist); overflow: hidden;
  }
  .grab-panel::before {
    content: ""; position: absolute; left: -150px; top: 50px;
    width: 440px; height: 440px; border-radius: 50%;
    background: var(--panel-circle); opacity: 0.8;
  }
  .grab {
    position: relative; text-align: center; padding-top: 156px; line-height: 1.15;
  }
  .grab-lead { color: var(--brand-teal); font-weight: 600; font-size: 27px; }
  .grab-main { color: var(--ink); font-weight: 600; font-size: 27px; }
  .grab-tail { color: var(--ink-soft); font-weight: 300; font-size: 24px; margin-top: 8px; }
  .pattern-block {
    position: absolute; left: 600px; top: 348px; width: 283px; height: 147px;
    background: linear-gradient(135deg, var(--pattern-teal) 0%, var(--pattern-light) 50%, var(--pattern-dark) 100%);
  }
</style>
</head>
<body>
  <main class="flyer">
    <div class="photo-pool" role="img" aria-label="Night photograph of a modern house with a lit courtyard pool under a violet dusk sky"></div>
    <svg class="wall-light" viewBox="0 0 600 495" aria-hidden="true">
      <polygon points="0,0 80,0 400,495 0,495" fill="var(--wall-lilac)" opacity="0.4"/>
    </svg>
    <div class="photo-terrace" role="img" aria-label="Photograph of a warmly lit outdoor terrace with lounge seating"></div>

    <h1 class="brand">HARBOURLINE<br>RETREATS<span class="brand-mark"></span></h1>

    <section class="grab-panel">
      <div class="grab">
        <p class="grab-lead">Holiday Rental</p>
        <p class="grab-main">Management</p>
        <p class="grab-tail">with a difference</p>
      </div>
    </section>

    <div class="pattern-block" role="img" aria-label="Decorative geometric pattern of teal and dark triangles"></div>
  </main>
</body>
</html>
```